Gift Card Designs for different ocassions

We supply gift cards to retailers. Most use one design and we would like to offer them different card designs for different occasions. They would be Birthday, christmas, Fathers day, Mothers day. Others would be You Rock, You are a star, Thank You, Awesome stuff, My Hero, Great effort and congratulations.
We really want a fun, funky design that makes the gift card pop.

Target Market(s)

Anyone who buys a gift card

Colors

Designer to choose colors to be used in the design.

Requirements
Nice to have
• just need exciting , funky designs that stand out.
Should not have
• dull boring colours that make it look to corporate

```html
<!DOCTYPE html>
<html lang="en">
<head>
<meta charset="utf-8">
<title>Birthday Gift Card</title>
<link href="https://fonts.googleapis.com/css2?family=Oswald:wght@600;700&family=Montserrat:wght@300;400;600&family=Parisienne&display=swap" rel="stylesheet">
<style>
  :root {
    --stage: #2a2527;
    --card-white: #ffffff;
    --title-blue: #5b9bd3;
    --ink: #2c2c2c;
    --band: #262626;
    --band-text: #f4f4f4;
    --back-light: #dde9ec;
    --back-mid: #c7dde3;
    --lettering: #4b2a5e;
    --gift-teal: #3fbf9f;
    --gift-purple: #a673c9;
    --gift-pink: #e8479a;
    --confetti-pink: #f27aa8;
    --confetti-blue: #74b8e6;
  }
  * { box-sizing: border-box; margin: 0; padding: 0; }
  html, body {
    width: 1200px; height: 675px; overflow: hidden;
    background: var(--stage);
  }
  .stage {
    position: relative; width: 1200px; height: 675px;
    display: flex; align-items: center; justify-content: center; gap: 40px;
  }
  .card {
    position: relative; width: 520px; height: 325px;
    border-radius: 6px; overflow: hidden;
    box-shadow: 0 10px 30px rgba(0,0,0,0.45);
  }

  /* Front */
  .card-front { background: var(--card-white); }
  .confetti {
    position: absolute; inset: 0;
    background:
      radial-gradient(circle at 20% 20%, var(--confetti-pink) 0 5px, transparent 6px),
      radial-gradient(circle at 62% 78%, var(--confetti-blue) 0 5px, transparent 6px),
      radial-gradient(circle at 88% 60%, var(--gift-teal) 0 5px, transparent 6px),
      radial-gradient(circle at 45% 12%, var(--gift-purple) 0 4px, transparent 5px),
      radial-gradient(circle at 8% 55%, var(--confetti-pink) 0 4px, transparent 5px),
      radial-gradient(circle at 75% 92%, var(--gift-pink) 0 4px, transparent 5px);
    opacity: 0.8;
  }
  .bunting {
    position: absolute; top: 0; right: 0; width: 210px; height: 95px;
    background: linear-gradient(200deg, #e94b8a 0%, #f6a623 25%, #4fbf6a 50%, #3a7fd6 75%, #8b4cc2 100%);
    clip-path: polygon(0 0, 100% 0, 100% 100%, 85% 55%, 60% 45%, 30% 25%);
    opacity: 0.9;
  }
  .gift-title {
    position: absolute; top: 38px; left: 300px;
    font-family: "Oswald", sans-serif; font-weight: 700;
    font-size: 54px; line-height: 0.95; letter-spacing: 2px;
    color: var(--title-blue); text-transform: uppercase;
  }
  .gift-title span { display: block; }
  .occasion {
    position: absolute; top: 138px; left: 196px; width: 300px;
    font-family: "Parisienne", cursive; font-weight: 400;
    color: var(--lettering); line-height: 0.95;
  }
  .occasion span { display: block; }
  .occasion .first { font-size: 56px; padding-left: 28px; }
  .occasion .second { font-size: 66px; }
  .gift-boxes {
    position: absolute; left: 24px; top: 150px; width: 150px; height: 160px;
    background: linear-gradient(180deg, var(--gift-teal) 0 30%, var(--gift-purple) 30% 70%, var(--gift-pink) 70% 100%);
    border-radius: 8px;
  }

  /* Back */
  .card-back { background: var(--back-light); font-family: "Montserrat", sans-serif; color: var(--ink); }
  .back-photo {
    position: absolute; inset: 0;
    background:
      radial-gradient(ellipse at 85% 85%, #f3d88a 0 14%, #f1b7bd 22%, transparent 40%),
      linear-gradient(135deg, var(--back-light), var(--back-mid));
    opacity: 0.9;
  }
  .back-content { position: relative; padding-top: 22px; }
  .validity {
    text-align: right; padding: 0 22px 5px;
    font-size: 10px; font-weight: 300;
  }
  .card-number {
    background: var(--band); color: var(--band-text);
    font-size: 19px; font-weight: 400; letter-spacing: 1.5px;
    text-align: center; padding: 11px 10px;
  }
  .terms {
    padding: 18px 26px 0; font-size: 13px; line-height: 1.55; font-weight: 400;
  }
  .redeem {
    padding: 18px 26px 2px; font-size: 13px; font-weight: 600;
    text-decoration: underline;
  }
  .website {
    padding: 0 26px; font-size: 14px; font-weight: 300; letter-spacing: 4px;
  }
</style>
</head>
<body>
<main class="stage">
  <article class="card card-front">
    <div class="confetti" role="img" aria-label="Scattered confetti, hearts and streamers"></div>
    <div class="bunting" role="img" aria-label="Colourful party bunting across the top corner"></div>
    <h1 class="gift-title"><span>Gift</span><span>Card</span></h1>
    <p class="occasion"><span class="first">Happy</span><span class="second">Birthday</span></p>
    <div class="gift-boxes" role="img" aria-label="Stacked teal, purple and pink gift boxes with bows"></div>
  </article>

  <article class="card card-back">
    <div class="back-photo" role="img" aria-label="Soft blurred photo of a birthday cupcake"></div>
    <div class="back-content">
      <p class="validity">This card is valid till 19-03-2019 only</p>
      <p class="card-number">1234 - 9587 - 6658 - 3574 - 6899 - 4589 - 3654</p>
      <p class="terms">It is a long established fact that a reader will be distracted by the readable content of a page when looking at its layout. The point of using Lorem Ipsum is that it has a more-or-less normal distribution of letters, as opposed to using 'Content here, content here'.</p>
      <p class="redeem">This gift card can only be utilised at:</p>
      <p class="website">www.partycardshop.com</p>
    </div>
  </article>
</main>
</body>
</html>
```